Business Card Design for Occupational Medicine Start Up Company

We need to design a professional business card. We are a healthcare company providing occupational medicine services to blue collar industries. We are professional, efficient and high quality service providers.

Target Market(s)

Blue Collar Industry: Shipbuilding, Ports, Trucking Companies; The Executives and Safety Officers for these companies

Industry/Entity Type

Healthcare

Contact Information for Business Card

Logo, Name, Title, Email, Phone

Other font styles liked:
• Please match our Brand Guide

Requirements
Must have
• Our Company Colors and Logo

```html
<!DOCTYPE html>
<html lang="en">
<head>
<meta charset="utf-8">
<title>CrewCare Clinics – Business Card</title>
<link href="https://fonts.googleapis.com/css2?family=Montserrat:wght@400;500;700&display=swap" rel="stylesheet">
<style>
  :root {
    --page: #e6e6e6;
    --card: #ffffff;
    --navy: #2a3384;
    --sky: #1fa0dd;
    --amber: #f2ad49;
    --ink: #3a3a3a;
  }
  * { box-sizing: border-box; margin: 0; padding: 0; }
  html, body { width: 1018px; height: 1200px; overflow: hidden; }
  body {
    background: var(--page);
    font-family: "Montserrat", Arial, sans-serif;
    color: var(--ink);
  }
  .brand-header {
    height: 170px;
    display: flex;
    align-items: center;
    justify-content: center;
    gap: 14px;
  }
  .brand-dot {
    width: 22px; height: 22px; border-radius: 50%;
    background: var(--navy);
  }
  .brand-name {
    font-weight: 700;
    font-size: 34px;
    letter-spacing: 1px;
    color: var(--navy);
  }
  .cards {
    display: flex;
    flex-direction: column;
    align-items: center;
    gap: 40px;
  }
  .card {
    position: relative;
    width: 760px;
    height: 434px;
    background: var(--card);
    overflow: hidden;
  }
  .card-stripes {
    position: absolute; inset: 0;
    width: 100%; height: 100%;
  }
  .card-front .front-brand {
    position: absolute;
    left: 130px; top: 190px;
    display: flex; align-items: center; gap: 12px;
  }
  .front-brand .brand-dot { width: 18px; height: 18px; background: var(--sky); }
  .front-brand .brand-name { font-size: 28px; color: var(--sky); }
  .holder {
    position: absolute;
    left: 52px; top: 92px;
  }
  .holder-name {
    font-weight: 700;
    font-size: 27px;
    color: var(--sky);
    letter-spacing: 0.2px;
  }
  .holder-title {
    font-size: 20px;
    font-weight: 400;
    letter-spacing: 0.6px;
    margin-top: 2px;
  }
  .contact-list {
    position: absolute;
    left: 54px; top: 284px;
    list-style: none;
    font-size: 14.5px;
    letter-spacing: 0.4px;
  }
  .contact-list li {
    display: flex; align-items: center; gap: 7px;
    height: 22px;
  }
  .contact-icon { width: 13px; height: 13px; flex: none; }
</style>
</head>
<body>
  <header class="brand-header">
    <span class="brand-dot"></span>
    <span class="brand-name">CREWCARE CLINICS</span>
  </header>

  <main class="cards">
    <section class="card card-front">
      <svg class="card-stripes" viewBox="0 0 742 424" preserveAspectRatio="none" aria-hidden="true">
        <polygon points="484,424 499,424 742,181 742,166" fill="var(--amber)"/>
        <polygon points="528,424 545,424 742,227 742,210" fill="var(--sky)"/>
        <polygon points="572,424 742,424 742,254" fill="var(--navy)"/>
      </svg>
      <div class="front-brand">
        <span class="brand-dot"></span>
        <span class="brand-name">CREWCARE CLINICS</span>
      </div>
    </section>

    <section class="card card-back">
      <svg class="card-stripes" viewBox="0 0 742 424" preserveAspectRatio="none" aria-hidden="true">
        <polygon points="484,424 499,424 742,181 742,166" fill="var(--amber)"/>
        <polygon points="528,424 545,424 742,227 742,210" fill="var(--sky)"/>
        <polygon points="572,424 742,424 742,254" fill="var(--navy)"/>
      </svg>
      <div class="holder">
        <h1 class="holder-name">DANIEL R. HOLLOWAY</h1>
        <p class="holder-title">Chief Executive Manager</p>
      </div>
      <ul class="contact-list">
        <li>
          <svg class="contact-icon" viewBox="0 0 12 12"><rect width="12" height="12" rx="2" fill="var(--amber)"/><path d="M3.5 3 L5 3 L5.6 4.6 L4.8 5.2 Q5.6 6.6 6.8 7.2 L7.4 6.4 L9 7 L9 8.5 Q5 9 3.5 3Z" fill="#fff"/></svg>
          +1 555-014-2288
        </li>
        <li>
          <svg class="contact-icon" viewBox="0 0 12 12"><rect width="12" height="12" rx="2" fill="var(--amber)"/><rect x="2.5" y="3.5" width="7" height="5" fill="#fff"/><path d="M2.5 3.5 L6 6.3 L9.5 3.5" stroke="var(--amber)" stroke-width="0.8" fill="none"/></svg>
          info@crewcareclinics.com
        </li>
        <li>
          <svg class="contact-icon" viewBox="0 0 12 12"><rect width="12" height="12" rx="2" fill="var(--amber)"/><circle cx="6" cy="6" r="3" fill="none" stroke="#fff" stroke-width="1"/><path d="M3 6 H9 M6 3 V9" stroke="#fff" stroke-width="0.7"/></svg>
          crewcareclinics.com
        </li>
        <li>
          <svg class="contact-icon" viewBox="0 0 12 12"><rect width="12" height="12" rx="2" fill="var(--amber)"/><path d="M6 10 L3.6 6.2 A2.8 2.8 0 1 1 8.4 6.2 Z" fill="#fff"/><circle cx="6" cy="4.9" r="1" fill="var(--amber)"/></svg>
          2750 Harbor Line Norfolk, VA 23510
        </li>
      </ul>
    </section>
  </main>
</body>
</html>
```